Brisbane IT support business needs our first business card

Hello we are a Brisbane based Information Technology company providing support and services to small and medium sized businesses. We provide a range of services and solutions.

The business name is Wattleridge Computer Services Group, or WCSG for short.

I am looking for a business card that looks professional (don't we all want that), but most importantly, it most utilize the colours in the logo attached.

Other business owners seeking our IT services, and also home users.

Business

• Please only use the blue/orange colours in logo attached

```html
<!DOCTYPE html>
<html lang="en">
<head>
<meta charset="utf-8">
<title>WCSG Business Card</title>
<link rel="stylesheet" href="https://fonts.googleapis.com/css2?family=Arimo:wght@400;700&display=swap">
<style>
  :root {
    --backdrop: #dddcdc;
    --card: #fdfdfd;
    --navy: #0d4560;
    --orange: #ee7d22;
  }
  * { margin: 0; padding: 0; box-sizing: border-box; }
  html, body { width: 1200px; height: 960px; overflow: hidden; }
  body {
    background: var(--backdrop);
    font-family: "Arimo", Arial, sans-serif;
    position: relative;
  }
  .card {
    position: absolute;
    left: 300px;
    width: 600px;
    height: 343px;
    background: var(--card);
    box-shadow: 0 12px 30px rgba(0,0,0,0.18);
    overflow: hidden;
  }
  .card--front { top: 90px; }
  .card--back { top: 527px; }

  .company {
    position: absolute;
    left: 56px;
    top: 84px;
    display: flex;
    align-items: center;
    gap: 14px;
  }
  .company__square {
    width: 16px;
    height: 16px;
    background: var(--orange);
    flex: none;
  }
  .company__name {
    font-size: 22px;
    font-weight: 400;
    color: var(--navy);
    line-height: 1.2;
  }

  .holder {
    position: absolute;
    right: 70px;
    top: 205px;
    font-size: 24px;
    color: var(--navy);
  }
  .holder__last { color: var(--orange); }

  .contact {
    position: absolute;
    left: 200px;
    top: 240px;
    list-style: none;
    font-size: 15px;
    line-height: 22px;
    color: var(--navy);
  }

  .band {
    position: absolute;
    right: 0;
    bottom: 18px;
    height: 12px;
    background: var(--orange);
  }
  .card--front .band { left: 260px; }
  .card--back .band { left: 198px; }
</style>
</head>
<body>
  <section class="card card--front">
    <div class="company">
      <span class="company__square"></span>
      <p class="company__name">Wattleridge Computer Services Group</p>
    </div>
    <p class="holder">Daniel <span class="holder__last">Reyes</span></p>
    <div class="band"></div>
  </section>

  <section class="card card--back">
    <div class="company">
      <span class="company__square"></span>
      <p class="company__name">Wattleridge Computer Services Group</p>
    </div>
    <ul class="contact">
      <li>p: (07) 3000 0000</li>
      <li>info@wattleridgecs.com</li>
      <li>www.wattleridgecs.com</li>
    </ul>
    <div class="band"></div>
  </section>
</body>
</html>
```